Food Packaging Design Project

We already have an established brand but feel that our packaging could be stronger. We would like the same logo outline , colour scheme and wording on the front and back... so that it is still recognisable to our customers but just a little more professional looking with the wow factor to help it stand out on the shelve.

We need both front and back design with colours on the back also.

The design must contain our registered logo design but can be added to.

The back doesn't have to be split into 2 columns as in the image provided.

The packets arn't the same as the old packs (as in picture attached) but instead will be pouches with solid edges.

We will need working files so that we can amend ourselves once the final design has been chosen.

Thanks in advance!

Reason: havent quite got what we are after, not enough designs submitted.

• The design must contain our registered logo... see image attached.

Must contain our colour that we currently have.

Must have the same writing on the front and back.

```html
<!DOCTYPE html>
<html lang="en">
<head>
<meta charset="utf-8">
<title>Lumo Noodles – Pouch Front</title>
<link rel="stylesheet" href="https://fonts.googleapis.com/css2?family=Righteous&family=Roboto+Condensed:ital,wght@0,700;1,700&display=swap">
<style>
  :root {
    --stage: #ececec;
    --pouch-cream: #f4f0b4;
    --pattern-olive: #d3d592;
    --band-red: #b8101a;
    --band-red-dark: #7e0a10;
    --band-red-light: #e0262c;
    --gold-light: #f6dc9a;
    --gold-dark: #c9953e;
    --ink-white: #ffffff;
    --banner-red: #a50f17;
    --banner-red-dark: #7d0a10;
    --tagline-ink: #2a2a2a;
    --pill-bg: #f5f5f5;
    --bowl-green: #7d9a3a;
    --steam-white: #f3f3ee;
  }
  * { box-sizing: border-box; margin: 0; padding: 0; }
  html, body { width: 1200px; height: 1000px; overflow: hidden; }
  body {
    background: var(--stage);
    display: flex; align-items: center; justify-content: center;
  }
  .pouch-front {
    position: relative;
    width: 620px; height: 800px;
    background: var(--pouch-cream);
    overflow: hidden;
  }
  .wave-pattern {
    position: absolute; inset: 0;
    background: linear-gradient(135deg, var(--pouch-cream) 0%, var(--pattern-olive) 50%, var(--pouch-cream) 100%);
    opacity: 0.55;
  }
  .bowl-illustration {
    position: absolute; left: 175px; top: 205px; width: 330px; height: 240px;
    border-radius: 24px;
    background: linear-gradient(180deg, var(--steam-white) 0%, var(--gold-light) 45%, var(--bowl-green) 100%);
  }
  .claim-band {
    position: absolute; left: 34px; top: 0; bottom: 0; width: 96px;
    background: linear-gradient(90deg, var(--band-red-dark), var(--band-red-light) 45%, var(--band-red) 100%);
    color: var(--ink-white);
    font-family: "Roboto Condensed", sans-serif;
    font-weight: 700;
  }
  .variant-name { position: absolute; top: 130px; left: 0; right: 0; text-align: center; font-size: 19px; }
  .variant-claims { position: absolute; top: 156px; left: 14px; list-style: none; font-size: 12px; font-style: italic; line-height: 16px; }
  .variant-claims li::before { content: "• "; }
  .zero-panel {
    position: absolute; top: 230px; left: 0; width: 96px; height: 240px;
    background: linear-gradient(180deg, var(--gold-light), var(--gold-dark));
  }
  .down-arrow { position: absolute; top: 195px; left: 0; width: 96px; height: 100px; }
  .zero-mark {
    position: absolute; top: 306px; left: 14px;
    font-family: "Righteous", sans-serif; color: var(--band-red-light);
    font-size: 62px; line-height: 1;
  }
  .zero-mark sup { font-size: 20px; vertical-align: top; }
  .zero-list { position: absolute; top: 385px; left: 18px; list-style: none; color: var(--band-red); font-size: 12px; font-style: italic; line-height: 14px; }
  .zero-list li::before { content: "• "; }
  .organic-dot { position: absolute; top: 600px; left: 37px; width: 22px; height: 22px; border-radius: 50%; background: var(--ink-white); }
  .organic-label { position: absolute; top: 630px; left: 0; right: 0; text-align: center; font-family: "Righteous", sans-serif; font-size: 12px; font-weight: 400; }
  .calorie-note { position: absolute; top: 654px; left: 0; right: 0; text-align: center; font-size: 17px; font-style: italic; line-height: 19px; }
  .name-banner {
    position: absolute; left: 110px; top: 420px; width: 480px; height: 150px;
    border-radius: 14px;
    background: linear-gradient(180deg, var(--banner-red) 0%, var(--banner-red-dark) 100%);
    display: flex; flex-direction: column; align-items: center; justify-content: center; gap: 14px;
  }
  .brand-block { display: flex; align-items: center; gap: 14px; }
  .brand-dot { width: 34px; height: 34px; border-radius: 50%; background: var(--ink-white); }
  .brand-name { font-family: "Righteous", sans-serif; font-size: 48px; font-weight: 400; color: var(--ink-white); letter-spacing: 1px; line-height: 1; }
  .tagline {
    width: 420px;
    padding: 6px 14px; border-radius: 14px;
    background: var(--pill-bg);
    font-family: "Righteous", sans-serif; font-size: 15px; color: var(--tagline-ink);
    text-align: center; font-variant: small-caps;
  }
</style>
</head>
<body>
  <main class="pouch-front">
    <div class="wave-pattern" role="img" aria-label="Repeating wavy noodle pattern in pale olive on cream"></div>
    <div class="bowl-illustration" role="img" aria-label="Illustration of a steaming green bowl of noodles"></div>

    <section class="claim-band">
      <p class="variant-name">ORIGINAL</p>
      <ul class="variant-claims">
        <li>FAT FREE</li>
        <li>WHEAT FREE</li>
      </ul>
      <div class="zero-panel"></div>
      <svg class="down-arrow" viewBox="0 0 96 100" aria-hidden="true">
        <polygon points="14,0 82,0 82,55 96,55 48,100 0,55 14,55" fill="var(--band-red)"/>
      </svg>
      <p class="zero-mark">0<sup>%</sup></p>
      <ul class="zero-list">
        <li>Net Cals</li>
        <li>Sugar</li>
        <li>Salt</li>
        <li>Gluten</li>
      </ul>
      <span class="organic-dot" aria-hidden="true"></span>
      <p class="organic-label">ORGANIC</p>
      <p class="calorie-note">8 Calories<br>per pack</p>
    </section>

    <div class="name-banner">
      <div class="brand-block">
        <span class="brand-dot" aria-hidden="true"></span>
        <h1 class="brand-name">Lumo Noodles</h1>
      </div>
      <p class="tagline">The Alternative to Pasta for Weight Loss</p>
    </div>
  </main>
</body>
</html>
```